Rental Product Flyer

We have an outdated flyer that we give to prospective customers. The flyer describes the products we rent and has pictures or drawings. Would like to update with better pictures or maybe use drawings if that is better. Need to use the new logo (attached) and only list the following stores and phone numbers: Northeast - Greensburg, PA 800.555.0143; Mid-Atlantic Portsmouth, VA 888.555.0178; Gulf Coast - Marlow Barge Basin - 281.555.0192; Louisiana - 225.555.0126

```html
<!DOCTYPE html>
<html lang="en">
<head>
<meta charset="utf-8">
<title>Harborline Rentals and Supply – Store Locations Flyer</title>
<link rel="stylesheet" href="https://fonts.googleapis.com/css2?family=Roboto:wght@700;900&display=swap">
<style>
  :root {
    --navy: #1b3d72;
    --white: #ffffff;
    --ink: #111111;
    --page-bg: #ececec;
    --photo-light: #f4f5f6;
    --photo-mid: #dfe2e5;
  }
  * { box-sizing: border-box; margin: 0; padding: 0; }
  html, body {
    width: 1200px; height: 1200px; overflow: hidden;
    background: var(--page-bg);
    font-family: "Roboto", Arial, sans-serif;
  }
  .flyer {
    position: absolute; left: 220px; top: 61px;
    width: 760px; height: 1078px;
    background: var(--white);
    overflow: hidden;
  }
  .equipment-photo {
    position: absolute; left: 22px; top: 202px; width: 706px; height: 870px;
    background: radial-gradient(ellipse at 45% 40%, var(--photo-mid) 0%, var(--photo-light) 60%, var(--white) 100%);
  }
  .flyer-shapes { position: absolute; left: 0; top: 0; width: 760px; height: 1078px; }
  .brand {
    position: absolute; right: 80px; top: 66px;
    display: flex; align-items: center; gap: 14px;
    color: var(--navy); font-weight: 900;
  }
  .brand-dot { width: 26px; height: 26px; border-radius: 50%; background: var(--navy); }
  .brand-name { font-size: 34px; line-height: 1.05; letter-spacing: .5px; text-transform: uppercase; }
  .store { position: absolute; font-weight: 700; font-size: 29px; line-height: 37px; letter-spacing: .3px; }
  .store-name { display: block; }
  .store-phone { display: flex; align-items: center; gap: 8px; font-size: 27px; position: absolute; white-space: nowrap; }
  .store--dark { color: var(--ink); }
  .store--light { color: var(--white); }
  .phone-icon { width: 30px; height: 30px; flex: none; }
  .phone-icon--solo { position: absolute; }
</style>
</head>
<body>
<main class="flyer">
  <div class="equipment-photo" role="img" aria-label="Faded photograph of an abrasive blasting pot on a skid frame"></div>

  <svg class="flyer-shapes" viewBox="0 0 608 862" aria-hidden="true">
    <!-- navy band behind northeast tile -->
    <path fill="var(--navy)" d="M0,240 Q110,198 253,196 L253,512 L0,512 Z"/>
    <!-- large right arc -->
    <path fill="var(--navy)" d="M608,178 C520,192 470,262 473,362 C477,520 540,720 608,862 Z"/>
    <!-- navy frame behind Louisiana tile -->
    <path fill="var(--navy)" d="M253,517 L495,517 C500,640 420,790 253,832 Z"/>
    <!-- northeast tile -->
    <path fill="var(--white)" d="M38,214 L205,214 Q236,214 236,250 L236,482 Q236,500 218,500 L34,500 Q16,500 16,482 L16,236 Q16,214 38,214 Z"/>
    <!-- mid-atlantic tile -->
    <path fill="var(--navy)" d="M290,239 L420,239 Q476,250 476,330 L476,480 Q476,499 458,499 L288,499 Q270,499 270,481 L270,259 Q270,239 290,239 Z"/>
    <!-- gulf coast tile -->
    <rect fill="var(--navy)" x="16" y="537" width="219" height="285" rx="20"/>
    <!-- Louisiana tile -->
    <path fill="var(--white)" d="M290,537 L460,537 Q478,537 478,560 C478,680 420,770 290,797 Q270,800 270,780 L270,557 Q270,537 290,537 Z"/>
  </svg>

  <div class="brand">
    <span class="brand-dot"></span>
    <span class="brand-name">Harborline<br>Rentals and Supply</span>
  </div>

  <section class="store store--dark" style="left:39px; top:398px;">
    <span class="store-name">Northeast</span>
    <span class="store-name">Greensburg,</span>
    <span class="store-name">PA</span>
    <span class="store-phone" style="left:0; top:141px;">
      <svg class="phone-icon" viewBox="0 0 24 24"><use href="#handset"/></svg>800.555.0143
    </span>
  </section>

  <section class="store store--light" style="left:354px; top:354px;">
    <span class="store-name">Mid-</span>
    <span class="store-name">Atlantic</span>
    <span class="store-name">Portsmouth,</span>
    <span class="store-name">VA</span>
    <svg class="phone-icon phone-icon--solo" viewBox="0 0 24 24" style="left:178px; top:154px;"><use href="#handset"/></svg>
    <span class="store-phone" style="left:0; top:198px;">888.555.0178</span>
  </section>

  <section class="store store--light" style="left:49px; top:752px;">
    <span class="store-name">Gulf Coast</span>
    <span class="store-name">Marlow Barge</span>
    <span class="store-name">Basin</span>
    <span class="store-phone" style="left:-10px; top:138px;">
      <svg class="phone-icon" viewBox="0 0 24 24"><use href="#handset"/></svg>281.555.0192
    </span>
  </section>

  <section class="store store--dark" style="left:354px; top:712px;">
    <span class="store-name">Louisiana</span>
    <svg class="phone-icon phone-icon--solo" viewBox="0 0 24 24" style="left:0; top:44px;"><use href="#handset"/></svg>
    <span class="store-phone" style="left:0; top:84px;">225.555.0126</span>
  </section>

  <svg width="0" height="0" style="position:absolute" aria-hidden="true">
    <symbol id="handset" viewBox="0 0 24 24">
      <path fill="var(--navy)" d="M6.6 3.2l2.3 3.4c.3.5.2 1.1-.2 1.5L7.3 9.4c.9 2.6 3 4.7 5.6 5.7l1.4-1.4c.4-.4 1-.5 1.5-.2l3.4 2.3c.5.3.7 1 .4 1.5l-1.2 2.2c-.4.7-1.2 1.1-2 .9C9.7 19.1 4.8 14.3 3.5 7.6c-.2-.8.2-1.6.9-2l2.2-1.2c.5-.3 1.2-.1 1.5.4z"/>
      <path fill="none" stroke="var(--navy)" stroke-width="1.8" stroke-linecap="round" d="M13.5 5.5a5 5 0 0 1 5 5M13.5 2a8.5 8.5 0 0 1 8.5 8.5"/>
    </symbol>
  </svg>
</main>
</body>
</html>
```